CD-/Plattencover für ein Harfen-Ensemble
Zielgruppe
Wir sind ein Ensemble von 3 Harfen und machen klassische Musik. Die Zielgruppe sind klassische Musikliebhaber von jung bis alt, die unkonventionelle Harfenmusik mögen. Das Programm hat spanischen Charakter.
Aufgabenstellung
Ein ansprechendes und schönes CD Cover, welches die Leidenschaft, Sehnsucht, Melancholie, Temperament der spanischen Musik um die Jahrhundertwende des 20. Jhdt. widerspiegelt.
Es sollte zumindest eine Harfe auf dem Cover zu erkennen sein, wenn auch nur stilistisch.
Fotos dürfen verwendet werden, falls auf dem Cover vorne, sollten die Menschen nur erahnt werden. Die Fotos dürfen gerne nach Belieben verwischt und bearbeitet werden, so dass man nur noch Züge oder Konturen erkennen kann.
Für die Rück-und Innenseite dürfte man die Personen auch erkennen.
Keine grellen Farben, eher warme Temperaturen.
Das Logo sollte irgendwo drauf sein, muss aber nicht auf die Vorderseite.
Der Name Velunessa sollte drauf. Unsere Namen Margit Ohlendorf, Liliane Brückner, Ottilie Kransfeld auf die Vorderseite. Velmorìa ist der Titel des Albums und sollte prominent sein.
Auf die Rückseite wirden die Stücke als Text darüber gelegt, bitte mit einbeziehen.
Denkbar wäre ein Design mit einem Schleier oder Spitzentuch (schwarz),oder einfach Spanische Spitze aks Element der in Verbindung mit der Harfe ist. Symbolisch für spanische Eleganz, Weiblichkeit, Tanz, Sehnsucht, Melancholie.....gedeckte Farben, Sepia, Gold, Bronze (Harfe).
Spanische aber schlicht-elegante Romantik.

```html
<!DOCTYPE html>
<html lang="de">
<head>
<meta charset="utf-8">
<title>Velmorìa – Velunessa drei Harfen</title>
<link href="https://fonts.googleapis.com/css2?family=Barlow:wght@400;500&family=Cormorant+Garamond:wght@400;500&display=swap" rel="stylesheet">
<style>
  :root {
    --stage: #e9e1d3;
    --veil-light: #b9bfa6;
    --veil-mid: #6c745c;
    --veil-dark: #2e3428;
    --harp-gold: #9a7a4c;
    --harp-bronze: #5a3c2c;
    --harp-silver: #c9c3b2;
    --night: #1a2232;
    --night-deep: #111825;
    --dusk: #4a3e34;
    --ivory: #f6f2ea;
    --muted: #c7ccd6;
  }
  * { margin: 0; padding: 0; box-sizing: border-box; }
  html, body { width: 817px; height: 1200px; overflow: hidden; }
  body {
    background: var(--stage);
    position: relative;
    font-family: "Barlow", "Helvetica Neue", Arial, sans-serif;
    color: var(--ivory);
  }

  /* ---------- front cover ---------- */
  .front-cover {
    position: absolute; left: 128px; top: 36px;
    width: 560px; height: 560px; overflow: hidden;
    box-shadow: 0 10px 24px rgba(60, 45, 30, .25);
  }
  .veil-photo {
    position: absolute; inset: 0;
    background:
      radial-gradient(ellipse at 80% 20%, var(--veil-light) 0%, transparent 55%),
      radial-gradient(ellipse at 15% 30%, #8a8a6a 0%, transparent 50%),
      linear-gradient(160deg, var(--veil-mid) 0%, var(--veil-dark) 55%, #3f4636 100%);
  }
  .harp-illustration {
    position: absolute; left: 0; right: 0; bottom: 0; height: 270px;
    background:
      linear-gradient(90deg, var(--harp-silver) 0%, var(--harp-bronze) 22%, var(--harp-gold) 30%, #3a362c 42%, var(--harp-gold) 50%, #3a362c 58%, var(--harp-gold) 70%, var(--harp-bronze) 78%, var(--harp-silver) 100%);
    opacity: .85;
    -webkit-mask: linear-gradient(180deg, transparent 0%, #000 18%);
            mask: linear-gradient(180deg, transparent 0%, #000 18%);
  }
  .ensemble-name {
    position: absolute; top: 136px; left: 0; right: 0; text-align: center;
    font-size: 17px; font-weight: 500; letter-spacing: 1.6px;
  }
  .member-list {
    position: absolute; top: 170px; left: 0; right: 0;
    display: flex; justify-content: center; gap: 18px;
    font-size: 12.5px; font-weight: 500; letter-spacing: 1.2px;
  }
  .album-title {
    position: absolute; top: 206px; left: 0; right: 0; text-align: center;
    font-family: "Cormorant Garamond", Georgia, serif;
    font-weight: 500; font-size: 60px; letter-spacing: 11px;
  }

  /* ---------- back cover ---------- */
  .back-cover {
    position: absolute; left: 128px; top: 636px;
    width: 560px; height: 440px; overflow: hidden;
    box-shadow: 0 10px 24px rgba(60, 45, 30, .25);
  }
  .ensemble-photo {
    position: absolute; inset: 0;
    background:
      radial-gradient(ellipse at 30% 25%, #6b5a4a 0%, transparent 45%),
      radial-gradient(ellipse at 80% 30%, #5e4638 0%, transparent 45%),
      linear-gradient(180deg, var(--dusk) 0%, #2a2e38 42%, var(--night) 68%, var(--night-deep) 100%);
  }
  .disc-runtime {
    position: absolute; left: 24px; top: 126px;
    font-size: 8px; letter-spacing: .4px;
  }
  .disc-title {
    position: absolute; left: 22px; top: 136px;
    font-family: "Cormorant Garamond", Georgia, serif;
    font-size: 27px; letter-spacing: 4px; font-weight: 400;
  }
  .tracklist {
    position: absolute; top: 186px; left: 24px; right: 24px;
    display: grid; grid-template-columns: 1fr 1fr; column-gap: 34px;
  }
  .track-column { display: flex; flex-direction: column; gap: 17px; }
  .track-column + .track-column { border-left: 1px solid rgba(246,242,234,.55); padding-left: 18px; margin-left: -18px; }
  .track { display: grid; grid-template-columns: 36px 1fr auto; font-size: 9.5px; line-height: 1.45; }
  .track-number { letter-spacing: .3px; }
  .track-composer { font-weight: 500; letter-spacing: .5px; }
  .track-era { font-size: 7px; margin-left: 4px; color: var(--muted); }
  .track-work { grid-column: 2; color: var(--muted); }
  .track-duration { grid-column: 3; grid-row: 2; color: var(--muted); }
  .back-footer {
    position: absolute; left: 24px; right: 24px; bottom: 16px;
    display: flex; align-items: flex-end;
  }
  .ensemble-wordmark {
    font-family: "Cormorant Garamond", Georgia, serif;
    font-size: 25px; font-weight: 400; letter-spacing: .5px;
    margin-right: 24px;
  }
  .footer-members { font-size: 7.5px; letter-spacing: .8px; line-height: 2.1; color: var(--muted); }
  .credits { margin-left: auto; text-align: right; font-size: 6.5px; line-height: 1.9; color: var(--muted); }
  .credits strong { font-weight: 500; color: var(--ivory); }
</style>
</head>
<body>

<section class="front-cover">
  <div class="veil-photo" role="img" aria-label="Fließender dunkler Schleierstoff in Oliv- und Graugrün"></div>
  <div class="harp-illustration" role="img" aria-label="Drei verzierte goldene und bronzene Harfensäulen mit Saiten"></div>
  <p class="ensemble-name">VELUNESSA DREI HARFEN</p>
  <p class="member-list"><span>MARGIT OHLENDORF</span><span>LILIANE BRÜCKNER</span><span>OTTILIE KRANSFELD</span></p>
  <h1 class="album-title">VELMORÌA</h1>
</section>

<section class="back-cover">
  <div class="ensemble-photo" role="img" aria-label="Die drei Harfenistinnen in dunkelblauen Kleidern vor einer efeubewachsenen Mauer"></div>
  <p class="disc-runtime">CD&nbsp; 76:02</p>
  <h2 class="disc-title">VELMORÌA</h2>

  <div class="tracklist">
    <div class="track-column">
      <div class="track"><span class="track-number">1-3</span><span class="track-composer">KOMPONIST 1<span class="track-era">(1700-1750)</span></span><span class="track-work">Sonata A-Dur für drei Harfen</span><span class="track-duration">12.03</span></div>
      <div class="track"><span class="track-number">4-6</span><span class="track-composer">KOMPONIST 2<span class="track-era">(1700-1750)</span></span><span class="track-work">Sonata A-Dur für drei Harfen</span><span class="track-duration">09.22</span></div>
      <div class="track"><span class="track-number">7-9</span><span class="track-composer">KOMPONIST 3<span class="track-era">(1700-1750)</span></span><span class="track-work">Sonata A-Dur für drei Harfen</span><span class="track-duration">11.51</span></div>
      <div class="track"><span class="track-number">10-12</span><span class="track-composer">KOMPONIST 4<span class="track-era">(1700-1750)</span></span><span class="track-work">Sonata A-Dur für drei Harfen</span><span class="track-duration">10.08</span></div>
    </div>
    <div class="track-column">
      <div class="track"><span class="track-number">13-14</span><span class="track-composer">KOMPONIST 5<span class="track-era">(1700-1750)</span></span><span class="track-work">Sonata A-Dur für drei Harfen</span><span class="track-duration">07.26</span></div>
      <div class="track"><span class="track-number">15-17</span><span class="track-composer">KOMPONIST 6<span class="track-era">(1700-1750)</span></span><span class="track-work">Sonata A-Dur für drei Harfen</span><span class="track-duration">09.23</span></div>
      <div class="track"><span class="track-number">18-20</span><span class="track-composer">KOMPONIST 7<span class="track-era">(1700-1750)</span></span><span class="track-work">Sonata A-Dur für drei Harfen</span><span class="track-duration">13.03</span></div>
      <div class="track"><span class="track-number">21-23</span><span class="track-composer">KOMPONIST 8<span class="track-era">(1700-1750)</span></span><span class="track-work">Sonata A-Dur für drei Harfen</span><span class="track-duration">10.00</span></div>
    </div>
  </div>

  <footer class="back-footer">
    <p class="ensemble-wordmark">velunessa</p>
    <p class="footer-members">MARGIT OHLENDORF<br>LILIANE BRÜCKNER<br>OTTILIE KRANSFELD</p>
    <p class="credits">© 2018 Velunessa drei Harfen<br>Aufnahme: Musterstadt, 01.10.2018<br>Fotos: Velunessa / Bildarchiv Lumora (cover)<br><strong>Printed in Germany</strong></p>
  </footer>
</section>

</body>
</html>
```